Talvero Engineering & Management Services Website

A professional website design that outlines Engineering and Management Services. The website is to be colour coordinated with the current logo (see attached). The webpage needs to be compatible with Wordpress to allow for easy changes to be made to the website for the user.
Required tabs for the page include:
- Civil Engineering
- Structural Engineering
- Project Management
- Business Management
- Project Controls
- Drafting
- Contact Us

Clean and efficient website that matches the services provided by the business.

Target Market(s)

New Customers to a very competitive market

Industry/Entity Type

Engineering

Number of Pages Required

5+ page

Requirements
Must have
• Clean with large stock photos

```html
<!DOCTYPE html>
<html lang="en">
<head>
<meta charset="utf-8">
<title>Talvero Engineering &amp; Management Services</title>
<link rel="stylesheet" href="https://fonts.googleapis.com/css2?family=Roboto:wght@300;400;500;700&display=swap">
<style>
:root{
  --orange:#ef6a1f;
  --orange-dark:#d95a12;
  --ink:#4a4a4a;
  --muted:#7a7a7a;
  --line:#dcdcdc;
  --grey-bg:#f1f1f1;
  --white:#ffffff;
  --button:#6b6b6b;
}
*{box-sizing:border-box;margin:0;padding:0}
html,body{width:1200px;height:2252px;overflow:hidden}
body{font-family:"Roboto",Arial,sans-serif;color:var(--ink);background:var(--white);position:relative}

/* header */
.site-header{height:88px;position:relative}
.brand{position:absolute;left:72px;top:18px;display:flex;align-items:center;gap:12px}
.brand-dot{width:40px;height:40px;border-radius:50%;background:var(--orange)}
.brand-name{font-size:30px;font-weight:700;color:var(--orange);letter-spacing:1px;text-transform:uppercase}
.phone{position:absolute;right:72px;top:28px;display:flex;align-items:center;gap:10px;font-size:22px;color:var(--ink)}
.phone-icon{width:30px;height:30px;border-radius:50%;background:var(--orange);display:flex;align-items:center;justify-content:center}
.main-nav{height:36px;background:var(--orange);display:flex;padding-left:60px}
.main-nav a{color:var(--white);text-decoration:none;font-size:14px;line-height:36px;padding:0 14px}
.main-nav a.active{background:var(--orange-dark)}

/* hero */
.hero{height:416px;position:relative;background:linear-gradient(100deg,#8f9aa6 0%,#c7ced6 35%,#a9b7c6 60%,#6f8296 100%)}
.hero-title{position:absolute;left:72px;top:170px;color:var(--white);font-size:42px;font-weight:400;line-height:1.25;text-shadow:0 2px 6px rgba(0,0,0,.35)}
.hero-dots{position:absolute;left:72px;bottom:22px;display:flex;gap:8px}
.hero-dots span{width:9px;height:9px;border-radius:50%;background:rgba(255,255,255,.6)}
.hero-dots span.on{background:var(--orange)}

/* section headings */
.section-mark{display:flex;align-items:center;justify-content:center;gap:16px}
.section-mark::before,.section-mark::after{content:"";width:470px;height:1px;background:var(--line)}
.section-mark i{width:34px;height:34px;border-radius:50%;background:var(--orange);display:block}
.section-title{text-align:center;font-size:34px;font-weight:400;color:var(--ink);margin-top:18px}
.section-title em{font-style:normal;color:var(--orange)}

/* welcome */
.welcome{height:500px;padding-top:72px}
.welcome-body{display:flex;gap:36px;padding:0 72px;margin-top:30px}
.welcome-photo{width:388px;height:232px;flex:none;background:linear-gradient(135deg,#b9c2cc,#e4e0da 55%,#8b98a6)}
.welcome-text p{font-size:14px;line-height:1.75;color:var(--muted);margin-bottom:14px}
.btn{display:inline-block;background:var(--button);color:var(--white);font-size:12px;font-weight:500;text-transform:uppercase;padding:10px 20px;text-decoration:none}

/* services */
.services{height:780px;background:var(--grey-bg);padding-top:20px}
.service-grid{display:grid;grid-template-columns:repeat(3,340px);gap:32px 20px;padding:0 72px;margin-top:28px}
.service-card{background:var(--white);height:300px;box-shadow:0 1px 3px rgba(0,0,0,.12)}
.service-photo{height:150px}
.service-card h3{color:var(--orange);font-size:20px;font-weight:500;padding:14px 16px 6px}
.service-card p{font-size:12.5px;line-height:1.6;color:var(--muted);padding:0 16px}
.service-card .more{display:block;font-size:11px;font-weight:700;color:var(--ink);text-transform:uppercase;padding:10px 16px}

/* news */
.news{height:348px;padding-top:40px}
.news-list{display:grid;grid-template-columns:repeat(3,340px);gap:20px;padding:0 72px;margin-top:30px}
.news-item{display:flex;gap:14px}
.news-date{width:50px;height:58px;background:var(--orange);color:var(--white);text-align:center;flex:none}
.news-date small{display:block;font-size:10px;background:var(--orange-dark);line-height:16px;text-transform:uppercase}
.news-date b{font-size:26px;font-weight:500;line-height:42px}
.news-item h4{color:var(--orange);font-size:15px;font-weight:500;margin-bottom:6px}
.news-item p{font-size:12.5px;line-height:1.6;color:var(--muted)}
.news-item .more{display:block;font-size:11px;font-weight:700;color:var(--ink);text-transform:uppercase;margin-top:8px}

/* footer */
.site-footer{height:124px;background:var(--orange);position:relative;color:var(--white)}
.footer-brand{position:absolute;left:72px;top:22px;display:flex;align-items:center;gap:10px}
.footer-brand .brand-dot{width:30px;height:30px;background:var(--white)}
.footer-brand .brand-name{color:var(--white);font-size:22px}
.legal{position:absolute;left:72px;top:70px;font-size:11px;line-height:1.6;opacity:.9}
.follow{position:absolute;right:72px;top:24px;text-align:right}
.follow span{font-size:14px}
.social{display:flex;gap:10px;margin-top:12px}
.social i{width:30px;height:30px;border:2px solid var(--white);border-radius:50%;display:block}
</style>
</head>
<body>

<header class="site-header">
  <div class="brand"><span class="brand-dot"></span><span class="brand-name">Talvero</span></div>
  <div class="phone">
    <span class="phone-icon">
      <svg width="16" height="16" viewBox="0 0 24 24"><path fill="#fff" d="M6.6 10.8a15 15 0 0 0 6.6 6.6l2.2-2.2c.3-.3.7-.4 1-.2 1.1.4 2.3.6 3.6.6.6 0 1 .4 1 1V20c0 .6-.4 1-1 1A17 17 0 0 1 3 4c0-.6.4-1 1-1h3.5c.6 0 1 .4 1 1 0 1.3.2 2.5.6 3.6.1.3 0 .7-.2 1z"/></svg>
    </span>
    123-555-0148
  </div>
</header>
<nav class="main-nav">
  <a class="active" href="#">Home</a><a href="#">About Us</a><a href="#">Civil Engineering</a><a href="#">Structural Engineering</a><a href="#">Project Management</a><a href="#">Business Management</a><a href="#">Project Controls</a><a href="#">Drafting</a><a href="#">Contact Us</a>
</nav>

<section class="hero" role="img" aria-label="Photo of an engineer in a hard hat with colleagues reviewing plans">
  <h1 class="hero-title">We are an Engineering and<br>Management Services Company</h1>
  <div class="hero-dots"><span class="on"></span><span></span><span></span></div>
</section>

<section class="welcome">
  <div class="section-mark"><i></i></div>
  <h2 class="section-title">Welcome to <em>Talvero Engineering &amp; Management Services</em></h2>
  <div class="welcome-body">
    <div class="welcome-photo" role="img" aria-label="Photo of a team of engineers working over drawings at a table"></div>
    <div class="welcome-text">
      <p>Our team delivers practical engineering and management solutions for clients across the region. From early planning to final handover, we work closely with owners, builders and designers to keep every project safe, efficient and on budget. We combine technical depth with clear communication so decisions are made quickly and with confidence.</p>
      <p>Whether you need a single structural review or full project controls, our engineers bring proven methods and honest advice to every stage of your work.</p>
      <a class="btn" href="#">Learn more</a>
    </div>
  </div>
</section>

<section class="services">
  <div class="section-mark"><i></i></div>
  <h2 class="section-title">Our <em>Services</em></h2>
  <div class="service-grid">
    <article class="service-card">
      <div class="service-photo" role="img" aria-label="Photo of civil engineers on a construction site" style="background:linear-gradient(135deg,#7d9ab8,#c9b89a)"></div>
      <h3>Civil Engineering</h3>
      <p>Practical design and review services delivered by experienced engineers, with clear reports and support through every stage.</p>
      <a class="more" href="#">Learn more</a>
    </article>
    <article class="service-card">
      <div class="service-photo" role="img" aria-label="Photo of a house model resting on building plans" style="background:linear-gradient(135deg,#d9c7a6,#efe9df)"></div>
      <h3>Structural Engineering</h3>
      <p>Practical design and review services delivered by experienced engineers, with clear reports and support through every stage.</p>
      <a class="more" href="#">Learn more</a>
    </article>
    <article class="service-card">
      <div class="service-photo" role="img" aria-label="Photo of a project manager in a hard hat with a team" style="background:linear-gradient(135deg,#c9ced4,#e9e6e1)"></div>
      <h3>Project Management</h3>
      <p>Practical design and review services delivered by experienced engineers, with clear reports and support through every stage.</p>
      <a class="more" href="#">Learn more</a>
    </article>
    <article class="service-card">
      <div class="service-photo" role="img" aria-label="Photo of a business meeting in an office" style="background:linear-gradient(135deg,#bfc6cf,#e6e2dc)"></div>
      <h3>Business Management</h3>
      <p>Practical design and review services delivered by experienced engineers, with clear reports and support through every stage.</p>
      <a class="more" href="#">Learn more</a>
    </article>
    <article class="service-card">
      <div class="service-photo" role="img" aria-label="Photo of engineers in safety vests checking a tablet on site" style="background:linear-gradient(135deg,#8fa3b8,#d3c48f)"></div>
      <h3>Project Controls</h3>
      <p>Practical design and review services delivered by experienced engineers, with clear reports and support through every stage.</p>
      <a class="more" href="#">Learn more</a>
    </article>
    <article class="service-card">
      <div class="service-photo" role="img" aria-label="Photo of technical drafting drawings with tools" style="background:linear-gradient(135deg,#e7e7e7,#bfc4c9)"></div>
      <h3>Drafting</h3>
      <p>Practical design and review services delivered by experienced engineers, with clear reports and support through every stage.</p>
      <a class="more" href="#">Learn more</a>
    </article>
  </div>
</section>

<section class="news">
  <div class="section-mark"><i></i></div>
  <h2 class="section-title">Latest <em>News</em></h2>
  <div class="news-list">
    <article class="news-item">
      <div class="news-date"><small>Jun</small><b>28</b></div>
      <div><h4>Project update from site...</h4><p>A short summary of recent work, new contracts and team news from our office.</p><a class="more" href="#">Learn more</a></div>
    </article>
    <article class="news-item">
      <div class="news-date"><small>Jun</small><b>28</b></div>
      <div><h4>Project update from site...</h4><p>A short summary of recent work, new contracts and team news from our office.</p><a class="more" href="#">Learn more</a></div>
    </article>
    <article class="news-item">
      <div class="news-date"><small>Jun</small><b>28</b></div>
      <div><h4>Project update from site...</h4><p>A short summary of recent work, new contracts and team news from our office.</p><a class="more" href="#">Learn more</a></div>
    </article>
  </div>
</section>

<footer class="site-footer">
  <div class="footer-brand"><span class="brand-dot"></span><span class="brand-name">Talvero</span></div>
  <p class="legal">Copyright © 2024 Talvero Engineering. All Rights Reserved.<br>Terms of Service | Privacy Policy</p>
  <div class="follow">
    <span>Follow Us</span>
    <div class="social"><i></i><i></i><i></i><i></i></div>
  </div>
</footer>

</body>
</html>
```